Dorrington Thermal Heating and Air Conditioning web page

This is a repair, installation and maintenance residential company. I don't do commercial. I need a web design that shows a company with 24/7 fast service that is easy for customers to contact me from. I am a Brackley /Tovex HVAC dealer and their logos can be on there also. I also sell IAQ products like Zenta- Orbit and I offer duct cleanings as well.

Industry/Entity Type

Hvac

Coding

Coded - Design and coding required

Number of Pages Required

2 page

```html
<!DOCTYPE html>
<html lang="en">
<head>
<meta charset="utf-8">
<title>Dorrington Thermal Heating and Air Conditioning</title>
<link href="https://fonts.googleapis.com/css2?family=Montserrat:ital,wght@0,400;0,500;0,600;0,700;1,400&family=Oswald:wght@500&display=swap" rel="stylesheet">
<style>
:root{
  --blue:#1ba4e6;
  --red:#ea1e27;
  --ink:#151515;
  --text:#5f5f5f;
  --grey-bg:#f1f1f1;
  --dark:#1c1c1c;
  --black:#0c0c0c;
  --white:#ffffff;
}
*{margin:0;padding:0;box-sizing:border-box}
html,body{width:1200px;height:4438px;overflow:hidden}
body{font-family:"Montserrat",sans-serif;color:var(--ink);background:var(--white);position:relative}
.abs{position:absolute}
.section{position:absolute;left:0;width:1200px}
.bar{position:absolute;height:4px;width:36px;background:var(--blue)}
.center-bar{left:582px}
.section-title{position:absolute;left:0;width:1200px;text-align:center;font-size:40px;font-weight:400}
.section-title b{font-weight:700}
.btn{position:absolute;display:flex;align-items:center;justify-content:center;color:var(--white);font-weight:600;font-size:18px;border-radius:3px;text-transform:uppercase}
.btn-red{background:var(--red)}
.btn-blue{background:var(--blue)}
.photo{position:absolute}

/* header */
.site-header{top:0;height:93px;background:var(--white)}
.brand{position:absolute;left:77px;top:24px;display:flex;align-items:center;gap:10px}
.brand-square{width:14px;height:14px;background:var(--red);flex:none}
.brand-name{font-weight:700;font-size:22px;color:var(--ink);line-height:1.05}
.brand-name small{display:block;font-size:10px;font-weight:600;letter-spacing:1px;color:var(--ink);margin-top:3px}
.nav{position:absolute;left:542px;top:38px;display:flex;gap:22px;font-size:14px;font-weight:500}
.nav .active{color:var(--red)}
.nav .active::before{content:"";display:inline-block;width:6px;height:6px;border-radius:50%;background:var(--red);margin-right:6px;vertical-align:middle}
.call-box{position:absolute;left:875px;top:0;width:325px;height:93px;background:var(--blue);border-bottom-left-radius:46px;color:var(--white)}
.call-box svg{position:absolute;left:32px;top:26px}
.call-box .small{position:absolute;left:84px;top:22px;font-size:13px}
.call-box .num{position:absolute;left:84px;top:40px;font-size:22px;font-weight:600}

/* hero */
.hero{top:93px;height:582px}
.hero-photo{left:0;top:0;width:1200px;height:582px;background:
  radial-gradient(ellipse 90px 50px at 300px 470px,rgba(40,170,195,.75),transparent 70%),
  radial-gradient(ellipse 110px 55px at 110px 500px,rgba(60,175,200,.6),transparent 70%),
  radial-gradient(ellipse 170px 90px at 620px 470px,rgba(70,100,150,.55),transparent 70%),
  radial-gradient(ellipse 120px 70px at 600px 360px,rgba(190,140,110,.5),transparent 70%),
  radial-gradient(ellipse 440px 150px at 450px 500px,rgba(150,150,150,.55),transparent 75%),
  radial-gradient(ellipse 60px 25px at 650px 40px,rgba(255,255,255,.95),transparent 70%),
  linear-gradient(90deg,#d9dde0 0%,#eef0f1 18%,#f4f5f5 50%,#eceeef 80%,#dfe2e3 100%)}
.hero-kicker{position:absolute;left:0;width:1200px;top:124px;text-align:center;color:var(--blue);font-size:24px}
.hero-title{position:absolute;left:0;width:1200px;top:158px;text-align:center;font-family:"Oswald",sans-serif;font-weight:500;font-size:44px;line-height:52px;color:var(--ink)}
.arrow{position:absolute;width:52px;height:52px;border-radius:50%;display:flex;align-items:center;justify-content:center}
.arrow-ghost{border:2px solid rgba(255,255,255,.9)}
.arrow-blue{background:var(--blue)}
.arrow-white{background:var(--white);box-shadow:0 2px 8px rgba(0,0,0,.15)}

/* welcome */
.welcome{top:675px;height:530px}
.corner-red{left:143px;top:74px;width:70px;height:60px;background:var(--red)}
.corner-blue{left:530px;top:385px;width:67px;height:73px;background:var(--blue)}
.welcome-photo{left:153px;top:84px;width:438px;height:364px;background:
  radial-gradient(ellipse 70px 60px at 110px 175px,rgba(30,150,220,.85),transparent 72%),
  radial-gradient(ellipse 110px 70px at 190px 300px,rgba(200,60,60,.45),transparent 72%),
  radial-gradient(ellipse 90px 130px at 300px 120px,rgba(90,100,110,.45),transparent 72%),
  linear-gradient(135deg,#f3f5f6,#dfe4e8 60%,#cfd6dc)}
.welcome .bar{left:658px;top:84px}
.kicker{position:absolute;font-size:13px;font-weight:500;letter-spacing:.5px}
.welcome-title{position:absolute;left:658px;top:130px;font-size:38px;font-weight:400}
.welcome-title b{font-weight:700}
.welcome-text{position:absolute;left:666px;top:212px;width:440px;font-size:14px;line-height:27px;color:var(--text)}

/* services */
.services{top:1205px;height:710px;background:var(--grey-bg)}
.services .bar{top:66px}
.services .section-title{top:84px}
.services-sub{position:absolute;left:0;width:1200px;top:140px;text-align:center;font-size:16px;color:#333}
.card{position:absolute;top:192px;width:288px;height:416px;background:var(--white);box-shadow:0 2px 10px rgba(0,0,0,.05)}
.card-photo{left:8px;top:8px;width:272px;height:198px}
.card-icon{position:absolute;left:8px;top:158px;width:48px;height:48px;background:var(--white);display:flex;align-items:center;justify-content:center}
.card h3{position:absolute;left:0;width:288px;top:238px;text-align:center;font-size:19px;font-weight:600}
.card p{position:absolute;left:24px;width:240px;top:282px;text-align:center;font-size:14px;line-height:27px;color:var(--text)}
.card .btn{top:390px;left:57px;width:177px;height:52px}

/* split band */
.band{top:1915px;height:385px}
.band-photo{left:0;top:0;width:1200px;height:385px;background:
  radial-gradient(ellipse 160px 120px at 520px 200px,rgba(40,110,180,.7),transparent 72%),
  radial-gradient(ellipse 200px 160px at 150px 90px,rgba(150,165,175,.55),transparent 72%),
  radial-gradient(ellipse 240px 180px at 980px 160px,rgba(200,205,200,.45),transparent 72%),
  radial-gradient(ellipse 90px 40px at 150px 360px,rgba(200,170,40,.5),transparent 72%),
  linear-gradient(90deg,#3c4750 0%,#2d363e 35%,#2a3036 60%,#4a4d4e 100%)}
.tag{position:absolute;top:150px;width:241px;height:86px;color:var(--white);padding:22px 0 0 0}
.tag .small{font-size:13px}
.tag .big{font-size:21px;font-weight:600;margin-top:4px}
.tag-cool{left:0;background:var(--blue);text-align:right;padding-right:22px}
.tag-heat{left:959px;background:var(--red);padding-left:30px}

/* testimonials */
.reviews{top:2300px;height:553px}
.reviews .bar{top:64px}
.reviews .section-title{top:82px}
.avatar{position:absolute;border-radius:50%;border:3px solid #e4e4e4}
.quote-dot{position:absolute;left:538px;top:247px;width:40px;height:40px;border-radius:50%;background:var(--red);color:var(--white);display:flex;align-items:center;justify-content:center;font-size:26px;font-weight:700;line-height:1}
.quote{position:absolute;left:310px;width:580px;top:322px;text-align:center;font-style:italic;font-size:16px;line-height:31px;color:var(--text)}
.client{position:absolute;left:0;width:1200px;top:440px;text-align:center;color:var(--blue);font-size:17px;font-weight:600}
.client-site{position:absolute;left:0;width:1200px;top:468px;text-align:center;font-size:13px;color:var(--text)}

/* products */
.products{top:2853px;height:620px}
.products .bar{top:62px}
.products .section-title{top:80px}
.product{position:absolute;top:160px;width:510px;height:250px;border:1px solid #e3e3e3}
.product-photo{left:0;top:0;width:250px;height:250px}
.product h3{position:absolute;left:280px;top:48px;font-size:20px;font-weight:600}
.product p{position:absolute;left:282px;top:88px;width:210px;font-size:14px;line-height:26px;color:var(--text)}
.product .more{position:absolute;left:282px;top:180px;font-size:13px;color:var(--red);font-weight:600}
.dealers{position:absolute;top:478px;left:0;width:1200px;display:flex;justify-content:center;gap:60px}
.dealer{text-align:center}
.dealer .name{font-size:34px;font-weight:700;color:var(--red);line-height:1}
.dealer .cap{font-size:13px;font-weight:500;color:#333;margin-top:6px}

/* contact */
.contact{top:3473px;height:531px}
.promise{position:absolute;left:0;top:0;width:600px;height:122px;background:var(--blue);color:var(--white);font-size:21px;font-weight:600;text-align:center;line-height:31px;padding-top:28px}
.map{left:0;top:122px;width:600px;height:409px;background:linear-gradient(160deg,#f4f4f4,#e7e9ea)}
.contact .bar{left:658px;top:76px}
.contact-title{position:absolute;left:660px;top:140px;font-size:38px;font-weight:500}
.field{position:absolute;height:58px;background:var(--white);border:1px solid #e1e1e1;font-size:14px;color:#777;padding:19px 20px}
.truck{left:918px;top:445px;width:282px;height:86px;background:radial-gradient(ellipse 140px 40px at 150px 50px,#2b2b2b,#0e0e0e 70%,transparent 72%)}

/* info bar */
.info{top:4004px;height:94px;background:var(--dark);color:var(--white)}
.info-item{position:absolute;top:0;height:94px;width:400px;display:flex;align-items:center;gap:16px;padding-left:44px;font-size:14px;white-space:nowrap}
.info-item svg{flex:none}
.info-item+.info-item{border-left:1px solid #3a3a3a}
.info-item.email{padding-left:30px;gap:14px;font-size:13.5px}

/* footer */
.footer{top:4098px;height:340px;background:var(--black);color:var(--white)}
.footer-brand{position:absolute;left:77px;top:34px;display:flex;align-items:center;gap:10px}
.footer-brand .brand-name{color:var(--white)}
.footer-brand .brand-name small{color:var(--white)}
.footer-text{position:absolute;left:77px;top:122px;width:360px;font-size:14px;line-height:27px;color:#d0d0d0}
.footer-more{position:absolute;left:77px;top:220px;font-size:14px;color:var(--blue);font-weight:600}
.col{position:absolute;top:64px}
.col h4{font-size:19px;font-weight:600;margin-bottom:24px}
.col li{list-style:none;font-size:14px;line-height:27px;color:#d0d0d0}
.news-input{position:absolute;left:828px;top:116px;width:295px;height:53px;background:var(--white);color:#777;font-size:14px;padding:17px 18px}
.footer .btn{left:828px;top:183px;width:155px;height:48px;font-size:17px}
.rule{position:absolute;left:77px;top:267px;width:1046px;height:1px;background:#2c2c2c}
.copy{position:absolute;left:77px;top:296px;font-size:14px;color:#d0d0d0}
.social{position:absolute;top:284px;width:40px;height:40px;border-radius:50%;border:2px solid var(--blue)}
</style>
</head>
<body>

<header class="section site-header">
  <div class="brand"><span class="brand-square"></span><div class="brand-name">Dorrington Thermal<small>HEATING AND AIR CONDITIONING</small></div></div>
  <nav class="nav"><span class="active">HOME</span><span>ABOUT</span><span>SERVICES</span><span>CONTACT</span></nav>
  <div class="call-box">
    <svg width="40" height="40" viewBox="0 0 24 24" fill="#fff"><path d="M6.6 10.8a15.1 15.1 0 0 0 6.6 6.6l2.2-2.2c.3-.3.7-.4 1-.2 1.1.4 2.3.6 3.6.6.6 0 1 .4 1 1V20c0 .6-.4 1-1 1A17 17 0 0 1 3 4c0-.6.4-1 1-1h3.5c.6 0 1 .4 1 1 0 1.3.2 2.5.6 3.6.1.3 0 .7-.2 1z"/></svg>
    <div class="small">We 24/7 Services Hours</div>
    <div class="num">555 010 2048</div>
  </div>
</header>

<section class="section hero">
  <div class="photo hero-photo" role="img" aria-label="Family relaxing on a grey sofa with teal cushions in a bright living room under a wall-mounted air conditioner"></div>
  <div class="hero-kicker">We 24/7 Services Hours</div>
  <h1 class="hero-title">Heating and Air Conditioning<br>Comfort Specialist</h1>
  <div class="arrow arrow-ghost" style="left:15px;top:375px"><svg width="14" height="22" viewBox="0 0 14 22"><path d="M11 2 3 11l8 9" fill="none" stroke="#fff" stroke-width="2.5"/></svg></div>
  <div class="arrow arrow-blue" style="left:1136px;top:375px"><svg width="14" height="22" viewBox="0 0 14 22"><path d="m3 2 8 9-8 9" fill="none" stroke="#fff" stroke-width="2.5"/></svg></div>
</section>

<section class="section welcome">
  <div class="abs corner-red"></div>
  <div class="abs corner-blue"></div>
  <div class="photo welcome-photo" role="img" aria-label="Technician in a blue hard hat servicing a ceiling air conditioning unit"></div>
  <div class="bar"></div>
  <div class="kicker" style="left:658px;top:100px">WELCOME &nbsp;TO</div>
  <h2 class="welcome-title"><b>Dorrington</b> Thermal</h2>
  <p class="welcome-text">We repair, install and maintain heating and cooling systems for homes across the region, with fast response any hour of the day and clear, honest pricing on every visit.</p>
  <div class="btn btn-red" style="left:666px;top:368px;width:177px;height:52px">Learn More</div>
</section>

<section class="section services">
  <div class="bar center-bar"></div>
  <h2 class="section-title"><b>Our</b> Services</h2>
  <div class="services-sub">We Provide 24/7 Services Hours</div>

  <div class="card" style="left:138px">
    <div class="photo card-photo" role="img" aria-label="Technician repairing a wall air conditioner" style="background:radial-gradient(ellipse 60px 90px at 120px 120px,rgba(60,90,130,.45),transparent 72%),linear-gradient(135deg,#f4f4f4,#d9dee2)"></div>
    <div class="card-icon"><svg width="34" height="34" viewBox="0 0 24 24" fill="none" stroke="#1ba4e6" stroke-width="2"><path d="M4 20 14 10M15 3a5 5 0 0 0 6 6l-3 3-6-6z"/><path d="m4 4 6 6M3 5l2-2" stroke="#151515"/></svg></div>
    <h3>Repair</h3>
    <p>Fast diagnosis and lasting fixes for furnaces and cooling units.</p>
    <div class="btn btn-blue">Learn More</div>
  </div>

  <div class="card" style="left:456px">
    <div class="photo card-photo" role="img" aria-label="Woman adjusting a newly installed air conditioner with a remote" style="background:radial-gradient(ellipse 70px 25px at 140px 40px,rgba(255,255,255,.95),transparent 72%),radial-gradient(ellipse 40px 60px at 60px 160px,rgba(200,110,90,.45),transparent 72%),linear-gradient(180deg,#cfd2d5,#9fa5aa)"></div>
    <div class="card-icon"><svg width="34" height="34" viewBox="0 0 24 24" fill="none" stroke="#ea1e27" stroke-width="2"><rect x="5" y="3" width="14" height="6" rx="1"/><path d="M12 9v12M8 21h8"/><path d="M8 14h8" stroke="#151515"/></svg></div>
    <h3>Installation</h3>
    <p>New heating and cooling systems fitted neatly and on time.</p>
    <div class="btn btn-red">Learn More</div>
  </div>

  <div class="card" style="left:775px">
    <div class="photo card-photo" role="img" aria-label="Technician cleaning the inside of an air conditioning unit" style="background:radial-gradient(ellipse 60px 90px at 220px 130px,rgba(40,80,160,.6),transparent 72%),linear-gradient(135deg,#eef1f3,#c6cfd7)"></div>
    <div class="card-icon"><svg width="34" height="34" viewBox="0 0 24 24" fill="none" stroke="#151515" stroke-width="2"><circle cx="12" cy="10" r="3"/><path d="M12 3v2M12 15v2M5 10h2M17 10h2M7 5l1.5 1.5M15.5 13.5 17 15M7 15l1.5-1.5M15.5 6.5 17 5"/><path d="M4 21h16" stroke="#1ba4e6"/></svg></div>
    <h3>Maintenance</h3>
    <p>Seasonal tune-ups that keep your system running efficiently.</p>
    <div class="btn btn-blue">Learn More</div>
  </div>
</section>

<section class="section band">
  <div class="photo band-photo" role="img" aria-label="Technician servicing an air conditioner beside a heating radiator"></div>
  <div class="tag tag-cool"><div class="small">Air Conditioning Services</div><div class="big">Cool it Down</div></div>
  <div class="tag tag-heat"><div class="small">Heating Services</div><div class="big">Heat it Up</div></div>
</section>

<section class="section reviews">
  <div class="bar center-bar"></div>
  <h2 class="section-title"><b>What Our</b> Client Say</h2>
  <div class="avatar" role="img" aria-label="Client portrait" style="left:461px;top:188px;width:70px;height:70px;background:#d9d9d9"></div>
  <div class="avatar" role="img" aria-label="Client portrait" style="left:551px;top:171px;width:104px;height:104px;background:#c9c9c9"></div>
  <div class="avatar" role="img" aria-label="Client portrait" style="left:668px;top:188px;width:70px;height:70px;background:#d9d9d9"></div>
  <div class="quote-dot">&ldquo;</div>
  <div class="arrow arrow-white" style="left:98px;top:257px"><svg width="12" height="20" viewBox="0 0 12 20"><path d="M10 2 2 10l8 8" fill="none" stroke="#151515" stroke-width="2.5"/></svg></div>
  <div class="arrow arrow-blue" style="left:1055px;top:257px"><svg width="12" height="20" viewBox="0 0 12 20"><path d="m2 2 8 8-8 8" fill="none" stroke="#fff" stroke-width="2.5"/></svg></div>
  <p class="quote">" The crew arrived the same night our heat went out and had the furnace running again within the hour. Friendly, tidy and fairly priced service. "</p>
  <div class="client">Client Name</div>
  <div class="client-site">someting.com</div>
</section>

<section class="section products">
  <div class="bar center-bar"></div>
  <h2 class="section-title"><b>IAQ</b> Products</h2>
  <div class="product" style="left:77px">
    <div class="photo product-photo" role="img" aria-label="Air purifier device glowing blue inside a duct" style="background:radial-gradient(ellipse 110px 30px at 160px 95px,rgba(120,200,255,.9),transparent 72%),radial-gradient(circle at 60% 45%,#2f7fcc,#0a1e3c 75%)"></div>
    <h3>Zenta- Orbit</h3>
    <p>Whole-home air purifier that fits inside your ductwork.</p>
    <div class="more">Read More &#9656;</div>
  </div>
  <div class="product" style="left:613px">
    <div class="photo product-photo" role="img" aria-label="Rotating brush cleaning the inside of a round air duct" style="background:radial-gradient(circle,#c9d6cf 0,#8e9498 18%,#5a5e61 55%,#2c2f31)"></div>
    <h3>Duct Cleanings</h3>
    <p>Thorough cleaning that clears dust from every air duct.</p>
    <div class="more">Read More &#9656;</div>
  </div>
  <div class="dealers">
    <div class="dealer"><div class="name">Tovex</div><div class="cap">Heating &amp; Air Conditioning</div></div>
    <div class="dealer"><div class="name">Brackley</div><div class="cap">Air Conditioning &amp; Heating</div></div>
  </div>
</section>

<section class="section contact">
  <div class="promise">We're not putting on Airs- our Work is<br>Guaranteed to satisfy.</div>
  <div class="photo map" role="img" aria-label="Map of the service area"></div>
  <div class="bar"></div>
  <div class="kicker" style="left:658px;top:92px">Get a Free Quote</div>
  <h2 class="contact-title">Contact Us</h2>
  <div class="field" style="left:663px;top:197px;width:219px">Name *</div>
  <div class="field" style="left:895px;top:197px;width:219px">Phone *</div>
  <div class="field" style="left:663px;top:269px;width:451px">Services *</div>
  <div class="field" style="left:663px;top:339px;width:451px">Email *</div>
  <div class="btn btn-red" style="left:663px;top:410px;width:134px;height:55px">Submit</div>
  <div class="photo truck" role="img" aria-label="Black company service pickup truck"></div>
</section>

<section class="section info">
  <div class="info-item" style="left:0"><svg width="34" height="34" viewBox="0 0 24 24" fill="none" stroke="#1ba4e6" stroke-width="1.6"><path d="M12 2a5 5 0 0 0-5 5c0 4 5 9 5 9s5-5 5-9a5 5 0 0 0-5-5z"/><circle cx="12" cy="7" r="2"/><path d="M4 22l2-6h12l2 6z"/></svg>Lorem ipsum simple text print text.</div>
  <div class="info-item" style="left:400px"><svg width="34" height="34" viewBox="0 0 24 24" fill="none" stroke="#1ba4e6" stroke-width="1.6"><path d="M6.6 10.8a15.1 15.1 0 0 0 6.6 6.6l2.2-2.2c.3-.3.7-.4 1-.2 1.1.4 2.3.6 3.6.6.6 0 1 .4 1 1V20c0 .6-.4 1-1 1A17 17 0 0 1 3 4c0-.6.4-1 1-1h3.5c.6 0 1 .4 1 1 0 1.3.2 2.5.6 3.6.1.3 0 .7-.2 1z"/></svg>Call Us On : 555 010 2048</div>
  <div class="info-item email" style="left:800px"><svg width="36" height="28" viewBox="0 0 24 18" fill="none" stroke="#1ba4e6" stroke-width="1.6"><rect x="1" y="1" width="22" height="16" rx="1"/><path d="m1 1 11 9 11-9"/></svg>Email Us : info@dorringtonthermal.com</div>
</section>

<footer class="section footer">
  <div class="footer-brand"><span class="brand-square" style="background:var(--blue)"></span><div class="brand-name">Dorrington Thermal<small>HEATING AND AIR CONDITIONING</small></div></div>
  <p class="footer-text">Trusted residential heating and cooling care, ready day and night for repairs, installs and upkeep.</p>
  <div class="footer-more">LEARN MORE &#9656;</div>
  <div class="col" style="left:491px"><h4>Sitemap</h4><ul><li>Home</li><li>About</li><li>Service</li><li>Contact</li></ul></div>
  <div class="col" style="left:658px"><h4>Services</h4><ul><li>Heating</li><li>Air Conditioning</li></ul></div>
  <div class="col" style="left:825px"><h4>Newsletter</h4></div>
  <div class="news-input">Enter Email *</div>
  <div class="btn btn-red">Subscribe</div>
  <div class="rule"></div>
  <div class="copy">&copy;Dorrington Thermal - 2020 All rights reserved.</div>
  <div class="social" aria-label="Social profile" style="left:991px"></div>
  <div class="social" aria-label="Social profile" style="left:1037px"></div>
  <div class="social" aria-label="Social profile" style="left:1083px"></div>
</footer>

</body>
</html>
```